Design for a Note buying company that attracts landlords and seller financed notes

I need a card designed. I want a simple clean front with my logo and contact info. On the back I want some big and bold words to get a message across.

Our Company buys Notes (mortgages) and we want to convey the sense of financial security. Our number one market that we pursue is tired landlords.

If you want to understand our business you can visit our website. www.lakeviewpaperfund.com

Do not use any Clip Art in the design, it will not be accepted. I want a custom designed card not something I could throw together myself. Simple clean and drive the message home.

Target Market(s)

Landlords, seller financed note holders

Industry/Entity Type

Mortgage

Contact Information for Business Card

Simple clean and bold. I need to grab the attention of the customer. It should convey a professional touch.

Font styles to use
Sans Serif

Colors
ec2229
ffffff

Requirements
Must have
• Clean front with logo and contact information
Front colors should match logo

Back should be bold and grab attention. Back colors are open to ideas
Nice to have
• The Back May use the phrase "No more Tentants, No more Toilets" "More Time, More Cash"

I'm open to other ideas about grabbing a landlords attention

I'm open to a square card design
I like cards with round corners as well
Should not have
• any clip art! must be custom designs.

```html
<!DOCTYPE html>
<html lang="en">
<head>
<meta charset="utf-8">
<title>Lakeview Paper Fund – Business Card</title>
<link rel="stylesheet" href="https://fonts.googleapis.com/css2?family=Poppins:wght@400;500;600;700;800&display=swap">
<style>
  :root {
    --brand-red: #ec2229;
    --white: #ffffff;
    --ink: #111111;
    --text-grey: #4a4a4a;
    --stage: #353535;
    --card-dark: #2b2b2b;
    --silver: #c9c9c9;
    --rule: #7a7a7a;
  }
  * { box-sizing: border-box; margin: 0; padding: 0; }
  html, body {
    width: 963px; height: 1200px; overflow: hidden;
    background: var(--stage);
    font-family: "Poppins", sans-serif;
  }
  .canvas { position: relative; width: 963px; height: 1200px; }

  .card {
    position: absolute; left: 223px;
    width: 577px; height: 329px;
    border-radius: 16px; overflow: hidden;
  }
  .card--front { top: 214px; background: var(--white); }
  .card--back  { top: 628px; background: var(--card-dark); }

  /* front */
  .brand-name {
    position: absolute;
    font-weight: 700; color: var(--ink);
    text-align: center; letter-spacing: 0.04em; line-height: 1.1;
  }
  .card--front .brand-name {
    left: 40px; width: 245px; top: 118px; font-size: 30px;
  }
  .brand-name__sub { display: block; font-size: 0.6em; letter-spacing: 0.22em; margin-top: 6px; }

  .divider {
    position: absolute; left: 302px; top: 83px;
    width: 1.5px; height: 163px; background: var(--rule);
  }
  .contact { position: absolute; left: 329px; top: 82px; color: var(--text-grey); }
  .contact__name {
    font-size: 19px; font-weight: 500; color: var(--brand-red);
    letter-spacing: 0.02em; line-height: 1.2;
  }
  .contact__title { font-size: 13px; color: #333; line-height: 1.2; }
  .contact__address { margin-top: 12px; font-size: 13px; line-height: 16px; }
  .contact__list { list-style: none; margin-top: 12px; }
  .contact__item {
    display: flex; align-items: center; gap: 7px;
    font-size: 13px; line-height: 16.5px;
  }
  .contact__icon { width: 11px; height: 11px; flex: none; fill: var(--brand-red); }

  /* back */
  .card--back .brand-name {
    left: 0; width: 100%; top: 100px;
    font-size: 48px; color: var(--silver); font-weight: 700;
  }
  .slogan-band {
    position: absolute; left: 0; top: 286px;
    width: 100%; height: 24px; background: var(--brand-red);
    color: var(--white); font-size: 11.5px; font-weight: 700;
    letter-spacing: -0.02em; text-transform: uppercase;
    display: flex; align-items: center; justify-content: center; gap: 7px;
  }
</style>
</head>
<body>
<main class="canvas">

  <section class="card card--front" aria-label="Card front">
    <div class="brand-name">LAKEVIEW<span class="brand-name__sub">PAPER FUND</span></div>
    <div class="divider"></div>
    <div class="contact">
      <h1 class="contact__name">DANIEL REYES</h1>
      <p class="contact__title">President</p>
      <p class="contact__address">4120 Birchwood Court<br>Anchorage, Alaska 34510</p>
      <ul class="contact__list">
        <li class="contact__item">
          <svg class="contact__icon" viewBox="0 0 24 24"><path d="M6.6 10.8a15 15 0 0 0 6.6 6.6l2.2-2.2c.3-.3.7-.4 1-.2 1.1.4 2.3.6 3.6.6.6 0 1 .4 1 1V20c0 .6-.4 1-1 1A17 17 0 0 1 3 4c0-.6.4-1 1-1h3.5c.6 0 1 .4 1 1 0 1.3.2 2.5.6 3.6.1.3 0 .7-.2 1z"/></svg>
          369-480-2217
        </li>
        <li class="contact__item">
          <svg class="contact__icon" viewBox="0 0 24 24"><path d="M7 1h10a2 2 0 0 1 2 2v18a2 2 0 0 1-2 2H7a2 2 0 0 1-2-2V3a2 2 0 0 1 2-2zm0 3v14h10V4z"/></svg>
          369-734-6190
        </li>
        <li class="contact__item">
          <svg class="contact__icon" viewBox="0 0 24 24"><path d="M2 5h20v14H2zm2 2v.5l8 5 8-5V7l-8 5z"/></svg>
          info@lakeviewpaperfund.com
        </li>
        <li class="contact__item">
          <svg class="contact__icon" viewBox="0 0 24 24"><circle cx="12" cy="12" r="11"/><path d="M6 8c2 0 3 1 3 3s2 2 2 4-1 3-1 5M15 4c0 2 1 3 3 3s2 2 3 3" stroke="#fff" stroke-width="1.8" fill="none"/></svg>
          www.lakeviewpaperfund.com
        </li>
      </ul>
    </div>
  </section>

  <section class="card card--back" aria-label="Card back">
    <div class="brand-name">LAKEVIEW<span class="brand-name__sub">PAPER FUND</span></div>
    <p class="slogan-band">
      <span>No more tentants</span><span>|</span>
      <span>No more toilets</span><span>|</span>
      <span>More time</span><span>|</span>
      <span>More cash</span>
    </p>
  </section>

</main>
</body>
</html>
```